E-Waste Recycling Company Business Card

New Electronic Recycling Company based in Long Island, New York called "Lady Rust-a-bunch" We take outdated computers, components, electrical wire, circuit breakers, ink cartridges, etc. We look mostly for donated items that we recycle for our customers but will pay for large quantities from businesses. The design should reflect that we are environmentally friendly and our unique 7Q Obliteration process that ensures all personal data is wiped clean off hard drives. Please use our attached logo
Industry/Entity Type
Electrical

```html
<!DOCTYPE html>
<html lang="en">
<head>
<meta charset="utf-8">
<title>Verdant Circuit – Business Card</title>
<link rel="stylesheet" href="https://fonts.googleapis.com/css2?family=Open+Sans:wght@400;600;700&display=swap">
<style>
  :root {
    --stage-center: #9a9b9e;
    --stage-edge: #3b3b3c;
    --card-light: #f4f4f4;
    --card-mid: #d4d5d6;
    --card-dark: #b9babb;
    --brand-green: #3dae3a;
    --ink: #2b2b2b;
    --strip-dark: #3f4042;
    --strip-light: #cfd0d1;
    --rivet: #f2f2f2;
  }
  * { margin: 0; padding: 0; box-sizing: border-box; }
  html, body { width: 1200px; height: 572px; overflow: hidden; }
  body {
    position: relative;
    font-family: "Open Sans", Arial, sans-serif;
    background: radial-gradient(ellipse 60% 75% at 50% 45%, var(--stage-center) 0%, #6f7073 55%, var(--stage-edge) 100%);
  }
  .card {
    position: absolute;
    top: 157px;
    width: 425px;
    height: 245px;
    overflow: hidden;
    background:
      linear-gradient(118deg, rgba(255,255,255,0) 30%, rgba(255,255,255,0.55) 42%, rgba(255,255,255,0) 52%),
      linear-gradient(100deg, var(--card-dark) 0%, var(--card-light) 35%, var(--card-mid) 65%, var(--card-light) 85%, var(--card-dark) 100%);
    box-shadow: 0 4px 10px rgba(0,0,0,0.45);
  }
  .card--front { left: 148px; }
  .card--back { left: 633px; }

  .metal-strip {
    position: absolute;
    left: 0; right: 0; bottom: 0;
    height: 17px;
    background: linear-gradient(90deg, var(--strip-dark) 0%, var(--strip-light) 30%, #8d8e90 55%, var(--strip-light) 78%, var(--strip-dark) 100%);
    border-top: 1px solid #6a6b6d;
  }
  .rivet {
    position: absolute;
    top: 5px;
    width: 5px; height: 5px;
    border-radius: 50%;
    background: var(--rivet);
    box-shadow: 0 0 1px #333;
  }

  .brand-mark {
    position: absolute;
    display: flex;
    flex-direction: column;
    align-items: center;
    gap: 10px;
    width: 160px;
  }
  .card--front .brand-mark { left: 220px; top: 88px; }
  .card--back .brand-mark { left: 117px; top: 88px; }
  .brand-mark__dot {
    width: 40px; height: 40px;
    border-radius: 50%;
    background: var(--brand-green);
  }
  .brand-mark__name {
    font-size: 17px;
    font-weight: 700;
    color: var(--brand-green);
    white-space: nowrap;
    line-height: 1.2;
  }

  .contact-block { position: absolute; left: 48px; top: 63px; color: var(--ink); }
  .contact-block__name { font-size: 16px; font-weight: 700; color: var(--brand-green); line-height: 1.1; }
  .contact-block__role { font-size: 9.5px; margin-top: 1px; }
  .contact-block__address { font-size: 9.5px; line-height: 14px; margin-top: 11px; }
  .contact-list { list-style: none; margin-top: 8px; font-size: 9.5px; }
  .contact-list li { display: flex; align-items: center; gap: 6px; height: 14.5px; }
  .contact-list svg { width: 10px; height: 10px; fill: var(--brand-green); flex: none; }
</style>
</head>
<body>

<section class="card card--front" aria-label="Business card front">
  <div class="contact-block">
    <p class="contact-block__name">Mara Kellwyn</p>
    <p class="contact-block__role">Managing Director</p>
    <p class="contact-block__address">Co. Street, Building<br>City/State,Zip Code</p>
    <ul class="contact-list">
      <li><svg viewBox="0 0 10 10"><path d="M2 0.5 L3.6 2.6 L2.7 3.7 Q3.8 6 6.3 7.3 L7.4 6.4 L9.5 8 L8.4 9.5 Q1.5 8.5 0.5 1.6 Z"/></svg>000-000-0000</li>
      <li><svg viewBox="0 0 10 10"><path d="M0.5 2 H9.5 V8.5 H0.5 Z M1.3 2.8 V7.7 H8.7 V2.8 L5 5.6 Z" fill-rule="evenodd"/></svg>info@youremail.com</li>
      <li><svg viewBox="0 0 10 10"><circle cx="5" cy="5" r="4.5"/><path d="M0.8 5 H9.2 M5 0.6 Q2.6 5 5 9.4 M5 0.6 Q7.4 5 5 9.4" stroke="#fff" stroke-width="0.7" fill="none"/></svg>www.yourwebsite.com</li>
    </ul>
  </div>
  <div class="brand-mark">
    <span class="brand-mark__dot"></span>
    <span class="brand-mark__name">Verdant Circuit</span>
  </div>
  <div class="metal-strip">
    <span class="rivet" style="left:26px"></span><span class="rivet" style="left:79px"></span>
    <span class="rivet" style="left:131px"></span><span class="rivet" style="left:184px"></span>
    <span class="rivet" style="left:237px"></span><span class="rivet" style="left:289px"></span>
    <span class="rivet" style="left:342px"></span><span class="rivet" style="left:395px"></span>
  </div>
</section>

<section class="card card--back" aria-label="Business card back">
  <div class="brand-mark">
    <span class="brand-mark__dot"></span>
    <span class="brand-mark__name">Verdant Circuit</span>
  </div>
  <div class="metal-strip">
    <span class="rivet" style="left:26px"></span><span class="rivet" style="left:79px"></span>
    <span class="rivet" style="left:131px"></span><span class="rivet" style="left:184px"></span>
    <span class="rivet" style="left:237px"></span><span class="rivet" style="left:289px"></span>
    <span class="rivet" style="left:342px"></span><span class="rivet" style="left:395px"></span>
  </div>
</section>

</body>
</html>
```